Talbrook Business Card Design

We need to update our current company business cards to something that is more professional. We are oilfield equipment manufacturing company. The company has and will continue to use a logo that is similar to the KORVEN aspirin logo. I would like to see that used alone in the design because that is how most companies recognize us. I also would not mind seeing the logo designed into something more "oilfield" to add some identification to our product line (i.e. maybe a oil rig coming off of it or something). Our units are primarily red, so I would like to stick with a red, black, white, and maybe grey color scheme. In addition to our logo. Our NPQ logo should be on back of card similar to the one I am attaching (FENWICKS). I am in process of getting a clean copy of that image. I am attaching a card (FENWICKS) from a previous company that I worked at that is now closed that I like the design of. I have also attached a current business card.
Updates

I have added our logo and an old business card from a company no longer in existence that I really like the design of. Please use those items in design and a color scheme of red and black. Grey and white can also be incorporated if needed. I need a design that will also translate easily to letterhead, brochures, documents, etc. I plan on also having those designed when I find the right designer.

Industry/Entity Type

Business

Contact Information for Business Card

Front

Talbrook Services (and logo)

Marla Pritchett
Management Rep

361-574-8826 Phone
361-574-8829 Fax
361-430-6658 Mobile
mpritchett@talbrookrigworks.example

Back:
Corpus Christi - Headquarters
4190 Sparrow Ln.
Corpus Christi, TX 78316

Texas - North Dakota - Pennsylvania

www.talbrookrigworks.example

Colors
ec2027
000000
5c5c5c
ffffff

Requirements
Nice to have
• The owners do like cards that have an expensive look to them. They feel that they have achieved that previously with raised ink. That feature or something that separates this card from other would be nice.
Should not have
• This card should not be SUPER modern. This is still an "old school" type owned company. The card should be professional thou.

```html
<!DOCTYPE html>
<html lang="en">
<head>
<meta charset="utf-8">
<title>Talbrook Services – Business Card</title>
<link rel="stylesheet" href="https://fonts.googleapis.com/css2?family=Open+Sans:wght@400;600;700&family=Arimo:wght@700&display=swap">
<style>
  :root {
    --red: #ec2027;
    --red-deep: #b5121a;
    --black: #000000;
    --charcoal: #1b1c1e;
    --charcoal-light: #2a2b2e;
    --grey: #5c5c5c;
    --badge: #3a3b3e;
    --text-light: #e6e6e6;
    --white: #ffffff;
    --backdrop: #bdbdbd;
  }
  * { box-sizing: border-box; margin: 0; padding: 0; }
  html, body {
    width: 1200px; height: 900px; overflow: hidden;
    background: var(--backdrop);
    font-family: "Open Sans", Arial, sans-serif;
  }
  .canvas {
    position: relative; width: 1200px; height: 900px;
    display: flex; align-items: center; justify-content: center; gap: 40px;
  }
  .card {
    position: relative; width: 540px; height: 310px;
    border-radius: 24px; overflow: hidden;
    box-shadow: 0 14px 30px rgba(0,0,0,0.28);
  }

  /* Back */
  .card-back {
    background: radial-gradient(ellipse at 40% 40%, var(--charcoal-light), var(--charcoal) 70%);
  }
  .cert-badge {
    position: absolute; left: 66px; top: 108px;
    width: 70px; height: 70px;
    background: var(--badge);
    border-radius: 4px;
  }
  .back-divider {
    position: absolute; left: 172px; top: 88px; width: 1px; height: 122px;
    background: var(--grey);
  }
  .back-address {
    position: absolute; left: 196px; top: 114px;
    color: var(--text-light); font-size: 14px; line-height: 19px;
    font-style: normal;
  }
  .back-web {
    position: absolute; left: 48px; bottom: 40px;
    color: var(--red); font-size: 13px; letter-spacing: 4.2px;
  }

  /* Front */
  .card-front { background: var(--charcoal); }
  .front-top {
    position: absolute; left: 0; top: 0; width: 100%; height: 160px;
    background: var(--white);
  }
  .front-band {
    position: absolute; left: 0; top: 160px; width: 100%; height: 9px;
    background: linear-gradient(var(--red), var(--red-deep));
  }
  .front-logo {
    position: absolute; left: 28px; top: 56px;
    display: flex; align-items: center; gap: 10px;
  }
  .front-logo .logo-circle {
    width: 40px; height: 40px; border-radius: 50%; background: var(--red);
  }
  .front-logo .logo-name {
    font-size: 26px; font-weight: 700; color: var(--red);
  }
  .company-name {
    position: absolute; left: 216px; top: 64px;
    font-family: "Arimo", Arial, sans-serif; font-weight: 700;
    font-size: 25px; color: var(--black); letter-spacing: 0.3px;
  }
  .person {
    position: absolute; left: 30px; top: 182px; color: var(--white);
  }
  .person-name { color: var(--red); font-size: 17px; font-weight: 600; line-height: 20px; }
  .person-title { font-size: 12px; line-height: 18px; }
  .contact-list {
    position: absolute; left: 30px; top: 232px; list-style: none;
    color: var(--white); font-size: 13.5px; line-height: 17px;
  }
  .contact-list li { display: flex; align-items: center; gap: 8px; }
  .contact-list svg { width: 13px; height: 13px; fill: var(--red); flex: none; }
</style>
</head>
<body>
<main class="canvas">

  <section class="card card-back" aria-label="Business card back">
    <div class="cert-badge" role="img" aria-label="Industry certification badge"></div>
    <div class="back-divider"></div>
    <address class="back-address">
      Corpus Christi - Headquarters<br>
      4190 Sparrow Ln.<br>
      Corpus Christi, TX 78316<br>
      Texas - North Dakota - Pennsylvania
    </address>
    <p class="back-web">www.talbrookrigworks.example</p>
  </section>

  <section class="card card-front" aria-label="Business card front">
    <div class="front-top"></div>
    <div class="front-band"></div>
    <div class="front-logo">
      <span class="logo-circle"></span>
      <span class="logo-name">Talbrook</span>
    </div>
    <h1 class="company-name">TALBROOK SERVICES</h1>
    <div class="person">
      <p class="person-name">Marla Pritchett</p>
      <p class="person-title">Management Rep</p>
    </div>
    <ul class="contact-list">
      <li>
        <svg viewBox="0 0 24 24"><path d="M6.6 10.8a15.2 15.2 0 0 0 6.6 6.6l2.2-2.2a1 1 0 0 1 1-.25 11.4 11.4 0 0 0 3.6.57 1 1 0 0 1 1 1V20a1 1 0 0 1-1 1A17 17 0 0 1 3 4a1 1 0 0 1 1-1h3.5a1 1 0 0 1 1 1c0 1.25.2 2.45.57 3.57a1 1 0 0 1-.25 1z"/></svg>
        361-574-8826
      </li>
      <li>
        <svg viewBox="0 0 24 24"><path d="M6 2h10v5H6zM3 8h18a1 1 0 0 1 1 1v10a1 1 0 0 1-1 1H3a1 1 0 0 1-1-1V9a1 1 0 0 1 1-1zm3 4v2h8v-2zm0 4v2h8v-2zm11-4v2h2v-2z"/></svg>
        361-574-8829
      </li>
      <li>
        <svg viewBox="0 0 24 24"><path d="M7 1h10a2 2 0 0 1 2 2v18a2 2 0 0 1-2 2H7a2 2 0 0 1-2-2V3a2 2 0 0 1 2-2zm0 3v14h10V4zm5 15.5a1.2 1.2 0 1 0 0 2.4 1.2 1.2 0 0 0 0-2.4z"/></svg>
        361-430-6658
      </li>
      <li>
        <svg viewBox="0 0 24 24"><path d="M2 5h20v14H2zm2 2v.5l8 5 8-5V7zm0 2.8V17h16V9.8l-8 5z"/></svg>
        mpritchett@talbrookrigworks.example
      </li>
    </ul>
  </section>

</main>
</body>
</html>
```